Label Design VelmoRest Capsules

Hello dear designers!

We run a brand for dietary supplements and are looking for a talented designer to help take our brand to the next level. We are planning to launch new products with fresh packaging and redesigned labels. Additionally, we would like to refresh our company logo to make it fit better on the packaging.

Important Info:

Our brand: VelmoPure – specializing in products for detoxification, sleep, and eye protection.
Our shop: www.velmopure.at – currently offering two main products:
VelmoPure (Detox Tincture)
Velmo Optic Guard (Blue Light Filter Glasses)
Project Goal: Initially, we are looking for a label design for our new product VelmoRest (sleep capsules). If we like the design, we would like to revise the label for our first product, VelmoPure, and potentially rework our logo to make it more compact and visually appealing on our packaging.

Design Preferences: We are fans of the design style of Farv Nutra and would love a design in a similar style – modern, clean, and premium – but with a unique touch that fits our brand. You will find some inspirations and ideas that we particularly like in the attachment.

Important:

Our packaging for VelmoRest is an 8 OZ jar (similar to the smaller jars used by Farv Nutra).
The label should be clear, appealing, and give the product a high-quality look.
An example of a previous design draft (which hasn’t fully convinced us yet), along with inspirations for our upcoming bundle (including VelmoPure, VelmoRest, and VelmoOptic Guard), is also attached.
Special Opportunity: The designer with the best concept will have the chance to collaborate with us long-term! We have two more brands in the pipeline and are looking for a reliable and creative partner for future projects. Generous compensation and tips are guaranteed.

We look forward to seeing creative and professional designs that will take our brand to the next level!

Target Market(s)

Germany

Industry/Entity Type

Supplement

Font styles to use
Sans Serif

Colors

Designer to choose colors to be used in the design.

Requirements
Must have
• Es sollte Hochwertig und Modern aussehen. Matt schwarzer hintergrund. less is more
Nice to have
• Maybe The head should be visible in the background.
Should not have
• it should not be colorful, and not too playful, it should definitely not look cheap!

```html
<!DOCTYPE html>
<html lang="de">
<head>
<meta charset="utf-8">
<title>VelmoRest Label</title>
<link rel="stylesheet" href="https://fonts.googleapis.com/css2?family=Oswald:wght@300;400;500;600&display=swap">
<style>
  :root{
    --stage:#e2e2e2;
    --label-top:#2f2f2f;
    --label-bottom:#1f1f1f;
    --tab:#1a1a1a;
    --gold-dark:#b88a45;
    --gold-light:#efdc9a;
    --gold-text:#c9a462;
    --cyan:#35b7e2;
    --white:#f2f2f2;
    --ink:#2a2418;
  }
  *{box-sizing:border-box;margin:0;padding:0}
  html,body{width:1200px;height:1200px;overflow:hidden}
  body{
    background:var(--stage);
    font-family:'Oswald',sans-serif;
    display:flex;align-items:center;justify-content:center;
  }
  .label{
    position:relative;
    width:760px;height:816px;
    background:linear-gradient(180deg,var(--label-top),var(--label-bottom));
    border-radius:6px;
    overflow:hidden;
  }
  .texture{
    position:absolute;inset:0;
    background:
      radial-gradient(ellipse 260px 200px at 90% 12%,rgba(0,0,0,.28),transparent 70%),
      radial-gradient(ellipse 240px 300px at 8% 40%,rgba(0,0,0,.22),transparent 70%),
      radial-gradient(ellipse 300px 220px at 85% 80%,rgba(0,0,0,.2),transparent 70%);
  }
  .head-art{
    position:absolute;left:220px;top:230px;width:360px;height:420px;
    background:radial-gradient(ellipse at 50% 45%,rgba(0,0,0,.25),transparent 70%);
  }
  .brand-tab{
    position:absolute;left:50%;top:0;transform:translateX(-50%);
    width:196px;height:196px;
    background:var(--tab);
    border-radius:0 0 98px 98px;
    display:flex;flex-direction:column;align-items:center;
    padding-top:66px;
  }
  .brand-name{
    color:var(--gold-text);
    font-weight:300;font-size:17px;line-height:1;letter-spacing:3px;
  }
  .brand-dot{
    margin-top:26px;width:30px;height:30px;border-radius:50%;
    border:1.5px solid var(--gold-text);
  }
  .product-title{
    position:absolute;left:0;right:0;top:246px;
    text-align:center;
    font-weight:500;font-size:116px;line-height:1.1;letter-spacing:1px;
  }
  .product-title span{
    background:linear-gradient(90deg,var(--gold-dark),var(--gold-light));
    -webkit-background-clip:text;background-clip:text;color:transparent;
  }
  .claim{
    position:absolute;left:50%;top:423px;transform:translateX(-50%);
    height:72px;white-space:nowrap;
    border:3px solid var(--cyan);border-radius:36px;
    padding:0 34px;
    color:var(--cyan);font-weight:500;font-size:34px;line-height:64px;
  }
  .benefits{
    position:absolute;left:50%;top:548px;transform:translateX(-50%);
    list-style:none;
  }
  .benefits li{
    color:var(--white);font-size:27px;font-weight:400;line-height:32px;
    white-space:nowrap;
    border-left:2px solid var(--cyan);padding-left:10px;margin-bottom:10px;
  }
  .amount{
    position:absolute;left:50%;top:745px;transform:translateX(-50%);
    height:56px;white-space:nowrap;
    background:linear-gradient(90deg,var(--gold-dark),var(--gold-light));
    border-radius:12px;
    padding:0 34px;
    color:var(--ink);font-weight:500;font-size:21px;line-height:56px;
  }
</style>
</head>
<body>
  <main class="label">
    <div class="texture"></div>
    <div class="head-art" role="img" aria-label="Faint line drawing of a head in profile behind the product name"></div>
    <div class="brand-tab">
      <span class="brand-name">VELMOPURE</span>
      <span class="brand-dot"></span>
    </div>
    <h1 class="product-title"><span>VELMO REST</span></h1>
    <p class="claim">FÖRDERT DIE TIEFSCHLAFPHASE</p>
    <ul class="benefits">
      <li>UNTERTITEL HINZUFÜGEN</li>
      <li>UNTERTITEL HINZUFÜGEN</li>
      <li>UNTERTITEL HINZUFÜGEN</li>
    </ul>
    <p class="amount">30 PORTIONEN | 60 KAPSELN</p>
  </main>
</body>
</html>
```